Crestline 14 Industrial Park Needs Website

We are looking for a website for a new project we are working on.
Project does not have a logo so just use text. Needs to be responsive and mobile friendly for all browsers and coded for both Android & IOS. SEO is also important. Want something visually grabbing that displays growth, quality and confidence.
WordPress or Joomla – must be desktop and mobile friendly with fast page load speed. Need the ability to edit ourselves.
See attached website brief for further information.
Land Sale/Lease/Development
Coded - Design and coding required
4 page

```html
<!DOCTYPE html>
<html lang="en">
<head>
<meta charset="utf-8">
<title>Lot Layout – Crestline 14 Industrial Park</title>
<link rel="stylesheet" href="https://fonts.googleapis.com/css2?family=Poppins:wght@400;500;600;700&display=swap">
<style>
  :root {
    --ink: #333333;
    --blue: #0b4fa6;
    --button: #0a72c2;
    --rule: #7fa9d6;
    --white: #ffffff;
    --band: #3f6fa8;
  }
  * { margin: 0; padding: 0; box-sizing: border-box; }
  html, body { width: 1109px; height: 1200px; overflow: hidden; background: var(--white); }
  body { position: relative; font-family: "Poppins", sans-serif; color: var(--ink); }

  .hero {
    position: absolute; left: 0; top: 0; width: 1109px; height: 243px;
    background:
      linear-gradient(180deg, rgba(255,255,255,.95) 0%, rgba(255,255,255,.6) 22%, rgba(255,255,255,0) 45%),
      linear-gradient(180deg, #b9c4b4 0%, #8f9a78 40%, #7c6f58 70%, #6b6a62 100%);
  }
  .brand { position: absolute; left: 69px; top: 30px; font-weight: 600; color: var(--ink); line-height: 1.05; }
  .brand-name { font-size: 27px; }
  .brand-sub { font-size: 16px; }
  .main-nav { position: absolute; top: 35px; left: 0; width: 1109px; height: 37px; }
  .main-nav a {
    position: absolute; top: 0; height: 37px; line-height: 37px;
    font-size: 12.6px; font-weight: 600; color: var(--ink); text-decoration: none;
  }
  .main-nav a.active {
    background: var(--blue); color: var(--white); border-radius: 19px;
    width: 124px; text-align: center;
  }
  .hero-title {
    position: absolute; left: 0; top: 118px; width: 1109px; text-align: center;
    font-size: 64px; font-weight: 700; color: var(--white); line-height: 1;
    text-shadow: 0 2px 6px rgba(0,0,0,.25);
  }

  .plan-map {
    position: absolute; left: 316px; top: 316px; width: 725px; height: 439px;
    background: linear-gradient(135deg, #5d6b5f 0%, #6c5a4e 40%, #5c7a86 65%, #6a5f55 100%);
  }
  .plan-mask { position: absolute; left: 316px; top: 358px; width: 85px; height: 355px; background: var(--white); }
  .intro { position: absolute; left: 69px; top: 383px; width: 320px; }
  .intro h2 { font-size: 37px; font-weight: 700; line-height: 40px; }
  .intro h2 .accent { color: var(--blue); display: block; }
  .intro-rule { position: absolute; left: 316px; top: 422px; width: 71px; height: 2px; background: var(--rule); }
  .intro p { margin-top: 20px; font-size: 13.6px; line-height: 23px; width: 320px; }
  .btn {
    position: absolute; left: 69px; top: 635px; width: 164px; height: 47px;
    background: var(--button); color: var(--white); border-radius: 24px;
    font-size: 14px; font-weight: 600; text-align: center; line-height: 47px; text-decoration: none;
  }

  .contact-band {
    position: absolute; left: 0; top: 833px; width: 1109px; height: 185px;
    background: linear-gradient(120deg, #36618f 0%, #4a7bb4 50%, #3c6aa0 100%);
    color: var(--white); text-align: center;
  }
  .contact-band h2 { position: absolute; top: 48px; width: 100%; font-size: 36px; font-weight: 700; line-height: 1; }
  .contact-rule { position: absolute; left: 471px; top: 105px; width: 167px; height: 2px; background: rgba(255,255,255,.7); }
  .contact-email { position: absolute; top: 122px; width: 100%; font-size: 18px; font-weight: 600; }
  .contact-email svg { vertical-align: -2px; margin-right: 8px; }

  .footer-nav a {
    position: absolute; top: 1057px; font-size: 13px; font-weight: 600; color: var(--ink); text-decoration: none;
  }
  .copyright { position: absolute; top: 1088px; width: 1109px; text-align: center; font-size: 13px; }
  .social { position: absolute; top: 1130px; left: 474px; display: flex; gap: 11px; }
  .social span { width: 20px; height: 20px; border-radius: 50%; background: #666; display: block; }
</style>
</head>
<body>
  <header class="hero" role="img" aria-label="Aerial photograph of an industrial development site">
  </header>
  <div class="brand">
    <div class="brand-name">Crestline 14</div>
    <div class="brand-sub">Industrial Park</div>
  </div>
  <nav class="main-nav">
    <a href="#" style="left:598px">HOME</a>
    <a href="#" style="left:677px">WHY ASHFORD?</a>
    <a href="#" class="active" style="left:792px">LOT LAYOUT</a>
    <a href="#" style="left:935px">CONTACT US</a>
  </nav>
  <h1 class="hero-title">LOT LAYOUT</h1>

  <div class="plan-map" role="img" aria-label="Aerial lot layout plan of the industrial park showing numbered lots and a stormwater facility"></div>
  <div class="plan-mask"></div>
  <div class="intro-rule"></div>
  <section class="intro">
    <h2>APPRAISAL <span class="accent">LOT LAYOUT</span></h2>
    <p>This Area Structure Plan is preliminary and will require modification. Provincial Transportation is considering our proposal for access to the property off Range Road 40 to alleviate significant costs related to access from Highway 14.</p>
  </section>
  <a href="#" class="btn">LEARN MORE</a>

  <section class="contact-band" role="img" aria-label="Photograph of a warehouse at dusk behind a blue overlay">
    <h2>CONTACT US</h2>
    <div class="contact-rule"></div>
    <div class="contact-email">
      <svg width="18" height="14" viewBox="0 0 18 14" fill="none" stroke="#fff" stroke-width="2"><rect x="1" y="1" width="16" height="12" rx="2"/><path d="M1 3l8 5 8-5"/></svg>info@crestline14.com
    </div>
  </section>

  <nav class="footer-nav">
    <a href="#" style="left:346px">HOME</a>
    <a href="#" style="left:425px">WHY ASHFORD?</a>
    <a href="#" style="left:562px">LOT LAYOUT</a>
    <a href="#" style="left:684px">CONTACT US</a>
  </nav>
  <p class="copyright">Copyright © 2024 Company Name All Rights Reserved</p>
  <div class="social" aria-label="Social links">
    <span></span><span></span><span></span><span></span><span></span>
  </div>
</body>
</html>
```